New Business Card Design Project

hello again,
i have an awful year and we were not able to complete our logo plan. we would like to use our #1 logo for business card design process. the primary colors for business card should be white background with orange & black letters. our business is mobil truck cranes. we deliver heavy stuff and unload cargo with crane that is mounted on our trucks.
here is our business card info:
HARBOR LIFT HAULERS, INC.
428 WESTCOTT AVE
MERRICK, NY 11542
OFFICE - 516 487 3091
DIRECT - 1 888 LIFT HAULS
MARK@HLHAULERS.COM
PLEASE also try to get our slogan on card .... "Our Loads Keep Rollin"
lastly please also put "24 hour Knuckleboom Service"
you can call me anytime 24/7 to discuss...my cell # is: 516 759 2036
please also list: Mark Delroy, President
Target Market(s)
Heavy Construction industry
Industry/Entity Type
heavy construction industry
Contact Information for Business Card
24 Hr Knuckleboom Service

```html
<!DOCTYPE html>
<html lang="en">
<head>
<meta charset="utf-8">
<title>Harbor Lift Haulers, Inc. — Business Card</title>
<link href="https://fonts.googleapis.com/css2?family=Arimo:wght@400;700&family=Montserrat:wght@600;800&display=swap" rel="stylesheet">
<style>
  :root {
    --page: #e6e6e6;
    --card: #ffffff;
    --card-soft: #f6f6f6;
    --ink: #1c1c1c;
    --ink-soft: #3a3a3a;
    --orange: #e8730d;
    --orange-edge: #c8610a;
    --ghost: #d9d9d9;
    --rule: #1c1c1c;
  }
  * { box-sizing: border-box; margin: 0; padding: 0; }
  html, body { width: 1200px; height: 801px; overflow: hidden; }
  body {
    background: var(--page);
    font-family: "Arimo", Arial, sans-serif;
    position: relative;
  }
  .card {
    position: absolute;
    top: 249px;
    width: 530px;
    height: 303px;
    background: linear-gradient(160deg, var(--card) 0%, var(--card-soft) 100%);
    border-bottom: 4px solid var(--orange-edge);
    border-right: 2px solid var(--orange-edge);
    box-shadow: 0 10px 24px rgba(0,0,0,.18);
    overflow: hidden;
    color: var(--ink);
  }
  .card--front { left: 50px; }
  .card--back { left: 620px; }

  /* front */
  .front-art {
    position: absolute;
    left: 30px; top: 60px;
    width: 360px; height: 240px;
    border-radius: 40px 40px 0 0;
    background: radial-gradient(ellipse at 50% 60%, rgba(200,200,200,.45), rgba(255,255,255,0) 70%);
  }
  .front-brand {
    position: absolute;
    right: 38px; top: 52px;
    display: flex; align-items: center; gap: 10px;
    font-family: "Montserrat", sans-serif;
    font-weight: 800;
    font-size: 17px;
    letter-spacing: .5px;
    color: var(--ink);
  }
  .brand-dot {
    width: 12px; height: 12px; border-radius: 50%;
    background: var(--orange);
  }
  .divider {
    position: absolute;
    left: 40px; right: 40px; top: 170px;
    height: 1.5px; background: var(--rule);
  }
  .holder { position: absolute; left: 40px; top: 118px; }
  .holder__name {
    font-family: "Montserrat", sans-serif;
    font-weight: 800;
    font-size: 20px;
    color: var(--orange);
    letter-spacing: .5px;
  }
  .holder__title { font-size: 13px; margin-top: 3px; color: var(--ink); }
  .contacts {
    position: absolute; left: 40px; top: 184px;
    list-style: none; font-size: 13px; letter-spacing: .4px; color: var(--ink);
  }
  .contacts li { display: flex; align-items: center; gap: 10px; height: 21px; }
  .contacts svg { width: 13px; height: 13px; flex: none; }
  .address {
    position: absolute; right: 40px; top: 186px;
    font-style: normal;
    text-align: left; font-size: 13px; line-height: 21px; letter-spacing: .4px; color: var(--ink);
  }

  /* back */
  .back-brand {
    position: absolute;
    left: 0; right: 0; top: 70px;
    text-align: center;
    font-family: "Montserrat", sans-serif;
    font-weight: 800;
    font-size: 26px;
    color: var(--ghost);
    letter-spacing: 1px;
  }
  .back-copy {
    position: absolute; left: 0; right: 0; top: 150px;
    text-align: center;
  }
  .slogan { font-size: 13px; letter-spacing: .4px; color: var(--ink); }
  .service-band {
    display: inline-block;
    margin-top: 6px;
    padding: 4px 26px;
    font-size: 17px; letter-spacing: .4px;
    color: var(--ink);
    background: linear-gradient(90deg, rgba(232,115,13,0) 0%, rgba(232,115,13,.75) 45%, rgba(232,115,13,.75) 55%, rgba(232,115,13,0) 100%);
  }
  .call-line {
    margin-top: 14px;
    font-size: 15px; font-weight: 700; letter-spacing: .3px; color: var(--ink);
  }
  .call-line__phone { color: var(--orange); font-weight: 400; font-size: 17px; margin-left: 8px; }
</style>
</head>
<body>

  <section class="card card--front" aria-label="Business card front">
    <div class="front-art" role="img" aria-label="Faint background illustration of a crane truck in front of a city skyline"></div>

    <div class="front-brand"><span class="brand-dot"></span>HARBOR LIFT HAULERS, INC.</div>

    <div class="holder">
      <p class="holder__name">MARK DELROY</p>
      <p class="holder__title">President</p>
    </div>

    <div class="divider"></div>

    <ul class="contacts">
      <li>
        <svg viewBox="0 0 16 16" aria-hidden="true"><path d="M4 1.5l2.2 3.2-1.4 1.6a9 9 0 0 0 4.9 4.9l1.6-1.4 3.2 2.2-1.2 2.2C8 14 2 8 1.8 2.7z" fill="none" stroke="#e8730d" stroke-width="1.5" stroke-linejoin="round"/></svg>
        516 487 3091
      </li>
      <li>
        <svg viewBox="0 0 16 16" aria-hidden="true"><rect x="4" y="1" width="8" height="14" rx="1.5" fill="none" stroke="#e8730d" stroke-width="1.5"/><line x1="7" y1="12.5" x2="9" y2="12.5" stroke="#e8730d" stroke-width="1.5"/></svg>
        1 888 LIFT HAULS
      </li>
      <li>
        <svg viewBox="0 0 16 16" aria-hidden="true"><rect x="1" y="3" width="14" height="10" fill="none" stroke="#e8730d" stroke-width="1.5"/><path d="M1 3l7 6 7-6" fill="none" stroke="#e8730d" stroke-width="1.5"/></svg>
        MARK@HLHAULERS.COM
      </li>
    </ul>

    <address class="address">
      428 WESTCOTT AVE<br>
      MERRICK, NY 11542
    </address>
  </section>

  <section class="card card--back" aria-label="Business card back">
    <div class="back-brand">HARBOR LIFT HAULERS, INC.</div>

    <div class="back-copy">
      <p class="slogan">Our Loads Keep Rollin</p>
      <p class="service-band">24 hour Knuckleboom Service</p>
      <p class="call-line">you can call me anytime 24/7 to discuss...my cell<span class="call-line__phone">516 759 2036</span></p>
    </div>
  </section>

</body>
</html>
```